Web Design for an Online Dating Web Site

We need an uncoded web design for a new online dating web site called zMatchy.net. Simplicity and boldness are the key factors in the successful design.
Please look at the requirements document attached for details.
Updates
Dear all,
Please AVOID USING A PICTURE OF A HAPPY COUPLE ON THE HOME PAGE of the site. We highly want to move away from this space as it makes our web site just like another dating web site.
We like something simple with web 2.0 look and feel. The examples in the Requirements Document are exactly the design we are after.
Regards
Tarn
Industry/Entity Type
Dating
Look and feel
Each slider illustrates characteristics of the customer's brand and the style your logo design should communicate.

```html
<!DOCTYPE html>
<html lang="en">
<head>
<meta charset="utf-8">
<title>zMatchy.net – Home</title>
<link href="https://fonts.googleapis.com/css2?family=PT+Sans+Narrow:wght@400;700&family=Open+Sans:wght@400;600&display=swap" rel="stylesheet">
<style>
:root{
  --pink:#e2287b;
  --pink-light:#f36aa6;
  --crimson:#9e1a3c;
  --crimson-dark:#7e1230;
  --grey-text:#7a7a7a;
  --dark:#2b2b2b;
  --footer-red:#ee3b4c;
  --teal:#38aac8;
  --teal-light:#59c4dd;
  --white:#ffffff;
}
*{margin:0;padding:0;box-sizing:border-box}
html,body{width:1200px;height:881px;overflow:hidden;background:var(--white)}
body{position:relative;font-family:"PT Sans Narrow",sans-serif}
.abs{position:absolute}

/* header */
.site-header{left:0;top:0;width:1200px;height:60px;background:var(--white)}
.brand{left:187px;top:10px;display:flex;align-items:center;gap:6px;font-weight:700;font-size:40px;color:var(--pink);line-height:1}
.brand-dot{width:14px;height:14px;border-radius:50%;background:var(--pink)}
.main-nav a{position:absolute;top:18px;height:22px;line-height:22px;font-weight:700;font-size:17px;color:#111;text-decoration:none}
.main-nav .active{background:var(--pink);color:var(--white);border-radius:11px;width:56px;text-align:center}
.header-rule{left:0;top:60px;width:1200px;height:8px;background:var(--crimson)}

/* hero */
.hero{left:0;top:68px;width:1200px;height:316px;overflow:hidden;background:linear-gradient(100deg,#f7a3c2 0%,#f27fa8 35%,#d8406e 65%,#8e1430 100%)}
.hero-band{left:0;top:249px;width:1200px;height:67px;background:var(--crimson)}
.hero-art{left:190px;top:34px;width:340px;height:282px;border-radius:8px;background:radial-gradient(circle at 50% 55%,rgba(255,255,255,.45),rgba(255,255,255,0) 70%)}
.hero-title{left:596px;top:82px;width:380px;font-weight:700;font-size:36px;line-height:51px;color:var(--white);text-shadow:0 2px 3px rgba(0,0,0,.25);white-space:nowrap}
.slider-arrow{width:38px;height:38px;border-radius:50%;background:rgba(255,255,255,.85);top:140px}

/* content */
.section-title{font-weight:700;font-size:21px;line-height:24px;color:var(--grey-text)}
.video-title{left:201px;top:412px;width:400px;text-align:center}
.video-caption{left:201px;top:640px;width:400px;text-align:center;font-size:25px;line-height:28px}
.play{left:317px;top:450px}
.login-title{left:690px;top:412px}
.login-box{left:690px;top:440px;width:324px;height:141px;border:1px solid #ddd;border-radius:8px;overflow:hidden;background:var(--white)}
.field{position:absolute;left:10px;width:171px;height:31px;border:2px solid #e4e4e4;border-radius:2px;font-family:"Open Sans",sans-serif;font-size:12px;color:#333;padding:6px 10px}
.forgot{position:absolute;left:208px;top:23px;font-family:"Open Sans",sans-serif;font-size:11.5px;color:#222;text-decoration:underline}
.signin-btn{position:absolute;left:200px;top:56px;width:105px;height:23px;border-radius:12px;background:var(--pink);color:var(--white);font-family:"Open Sans",sans-serif;font-size:11.5px;line-height:23px;padding-left:24px}
.signin-btn::after{content:"";position:absolute;right:0;top:0;width:18px;height:23px;border-radius:0 12px 12px 0;background:var(--crimson-dark)}
.social-strip{position:absolute;left:0;top:95px;width:324px;height:46px;background:linear-gradient(#f05aa2,#e2287b)}
.social-strip .or{position:absolute;left:21px;top:10px;font-weight:700;font-size:23px;color:var(--white)}
.social-strip .more{position:absolute;left:264px;top:13px;font-weight:700;font-size:16px;color:var(--white)}
.social-icon{position:absolute;top:6px;width:33px;height:33px;border-radius:4px;background:rgba(255,255,255,.85)}
.signup-box{left:690px;top:598px;width:324px;height:102px;border:1px solid #d9d9d9;border-radius:8px;padding:3px}
.signup-btn{width:100%;height:100%;border-radius:6px;background:linear-gradient(var(--teal-light),var(--teal));color:var(--white);font-weight:700;font-size:46px;text-align:center;line-height:94px;text-shadow:0 2px 2px rgba(0,0,0,.25)}

/* footer */
.site-footer{left:0;top:728px;width:1200px;height:153px;background:var(--dark)}
.footer-heading{font-weight:700;font-size:20px;color:var(--footer-red)}
.footer-links{left:187px;top:771px;list-style:none}
.footer-links li{font-weight:700;font-size:14px;color:var(--white);height:21px;line-height:21px}
.footer-links li::before{content:"→";color:var(--footer-red);margin-right:5px}
.share-icon{width:28px;height:28px;border-radius:4px;background:#5c6a78}
.copy{right:186px;top:757px;font-family:"Open Sans",sans-serif;font-size:12px;color:var(--white);text-align:right}
.footer-brand{right:186px;top:784px;display:flex;align-items:center;gap:6px;font-weight:700;font-size:38px;color:#dcdcdc}
.footer-brand .brand-dot{background:#dcdcdc}
.legal{right:186px;top:841px;font-family:"Open Sans",sans-serif;font-size:12px;color:var(--white)}
</style>
</head>
<body>
<header class="abs site-header">
  <div class="abs brand"><span>zMatchy</span><span class="brand-dot"></span></div>
  <nav class="main-nav">
    <a class="active" style="left:629px">Why</a>
    <a style="left:734px">How It Works</a>
    <a style="left:857px">Sign Up</a>
    <a style="left:965px">Our Blog</a>
  </nav>
</header>
<div class="abs header-rule"></div>

<section class="abs hero">
  <div class="abs hero-band"></div>
  <div class="abs hero-art" role="img" aria-label="Illustration of two smiling cartoon balls, pink and blue, under gender symbols with small birds"></div>
  <div class="abs slider-arrow" style="left:169px">
    <svg width="38" height="38"><path d="M22 12 L15 19 L22 26" stroke="#222" stroke-width="3.5" fill="none" stroke-linecap="round"/></svg>
  </div>
  <h1 class="abs hero-title">zMatchy provides a new<br>and different way to meet<br>people online</h1>
  <div class="abs slider-arrow" style="left:993px;background:rgba(255,255,255,.55)">
    <svg width="38" height="38"><path d="M16 12 L23 19 L16 26" stroke="#222" stroke-width="3.5" fill="none" stroke-linecap="round"/></svg>
  </div>
</section>

<h2 class="abs section-title video-title">Want to Know How It Works...</h2>
<svg class="abs play" width="168" height="168" viewBox="0 0 168 168">
  <defs><linearGradient id="ring" x1="0" y1="0" x2="0" y2="1"><stop offset="0" stop-color="#e2287b"/><stop offset="1" stop-color="#a01a45"/></linearGradient></defs>
  <circle cx="84" cy="84" r="76" fill="#fff" stroke="url(#ring)" stroke-width="16"/>
  <path d="M62 48 L126 84 L62 120 Z" fill="var(--pink)"/>
</svg>
<p class="abs section-title video-caption">Watch a Vedio</p>

<h2 class="abs section-title login-title">Already a Member?&nbsp; Sign-In Now</h2>
<form class="abs login-box">
  <div class="field" style="top:14px">User Name</div>
  <div class="field" style="top:53px">Password</div>
  <a class="forgot">Forgot Password?</a>
  <div class="signin-btn">SIGN-IN</div>
  <div class="social-strip">
    <span class="or">OR</span>
    <span class="social-icon" style="left:60px"></span>
    <span class="social-icon" style="left:102px"></span>
    <span class="social-icon" style="left:143px"></span>
    <span class="social-icon" style="left:184px"></span>
    <span class="social-icon" style="left:225px"></span>
    <span class="more">More...</span>
  </div>
</form>
<div class="abs signup-box"><div class="signup-btn">SIGN UP NOW</div></div>

<footer class="abs site-footer"></footer>
<h3 class="abs footer-heading" style="left:187px;top:744px">Read More</h3>
<ul class="abs footer-links">
  <li>Why zMatchy</li><li>How it works</li><li>Sign Up</li><li>Login</li><li>About Us</li>
</ul>
<h3 class="abs footer-heading" style="left:515px;top:744px">Share This</h3>
<span class="abs share-icon" style="left:515px;top:771px"></span>
<span class="abs share-icon" style="left:550px;top:771px"></span>
<span class="abs share-icon" style="left:585px;top:771px"></span>
<span class="abs share-icon" style="left:620px;top:771px"></span>
<span class="abs share-icon" style="left:515px;top:802px"></span>
<span class="abs share-icon" style="left:550px;top:802px"></span>
<span class="abs share-icon" style="left:585px;top:802px"></span>
<span class="abs share-icon" style="left:620px;top:802px"></span>
<p class="abs copy">© 2011 zMatchy &nbsp;|&nbsp; All Rights Reserved</p>
<div class="abs footer-brand"><span>zMatchy.net</span><span class="brand-dot"></span></div>
<p class="abs legal">Privacy Policy &nbsp;|&nbsp; Terms &amp; Conditions</p>
</body>
</html>
```